Brochure Design Project

We need a design for a company based in kingdom of saudi arabia, which is an event management company called lumevara...the design must match the logo and should be very creatuve,,

What We Serve
We conceptualize and implement events and campaigns of all sizes and calibres. As experts in our industry, we maintain national strategic relationships and an extensive knowledge base that allow us the resources to execute events at any level. Our understanding of customer service and commitment gives us a significant advantage above the rest. We are very flexible with the services that we offer and can offer our complete list of services in coordinating your requirements.
Our Services are designed to allow you to choose how best we can help to stage your occasion from conception to completion.
We aim to listen to your needs to match them to our services is what makes us strong.

Our Speciality
• Event Management Services
• Corporate Meetings & Conferences
• Corporate Training Programs
• Grand Openings
• Event Theme & Decor Styling
• Product Launch & Brand Awareness
• Lavish Social Events & Gala Dinners
• Marketing & PR Campaigns
Updates

HI

Please note that I will give high preference to 3d designs

dear all

thanks for the hard work....please try to show me designs with a balck base as well

Target Market(s)

hotels, automotive industries, resturants and etc

Industry/Entity Type

Events

Requirements
Must have
• the logo matching theme
Nice to have
• attached is my logo of lumevara and samples of brchures
Should not have
• less then 5 pages

```html
<!DOCTYPE html>
<html lang="en">
<head>
<meta charset="utf-8">
<title>Lumevara – About the company</title>
<link href="https://fonts.googleapis.com/css2?family=Crimson+Text:ital,wght@0,600;1,400&display=swap" rel="stylesheet">
<style>
  :root {
    --ink: #000000;
    --paper: #ffffff;
    --teal: #108f96;
    --teal-deep: #0e8a92;
    --green: #78c832;
    --mint: #3ee3ab;
    --lime: #c8df26;
    --leaf: #aee64e;
    --olive: #a0911a;
    --moss: #9ec94a;
  }
  html, body {
    margin: 0;
    padding: 0;
    overflow: hidden;
    background: var(--ink);
  }
  .page {
    position: relative;
    width: 900px;
    height: 1200px;
    background: var(--ink);
    overflow: hidden;
    font-family: "Crimson Text", Georgia, serif;
    color: var(--paper);
  }
  .tile { position: absolute; }
  .teal { background: var(--teal); }
  .teal-deep { background: var(--teal-deep); }
  .green { background: var(--green); }
  .mint { background: var(--mint); }
  .lime { background: var(--lime); }
  .leaf { background: var(--leaf); }
  .olive { background: var(--olive); }
  .moss { background: var(--moss); }

  .page-title {
    position: absolute;
    left: 0;
    width: 830px;
    top: 152px;
    margin: 0;
    text-align: center;
    font-weight: 600;
    font-size: 58px;
    letter-spacing: 2.5px;
    line-height: 1;
    white-space: nowrap;
  }
  .intro, .body-copy {
    position: absolute;
    margin: 0;
    font-style: italic;
    font-weight: 400;
    font-size: 34px;
    letter-spacing: 1.2px;
    white-space: nowrap;
  }
  .intro { left: 62px; top: 268px; line-height: 42.7px; }
  .body-copy { left: 222px; top: 492px; line-height: 44.7px; }

  .photo-frame {
    position: absolute;
    left: 420px;
    top: 251px;
    width: 480px;
    height: 205px;
    background: var(--paper);
  }
  .photo {
    position: absolute;
    left: 24px;
    top: 26px;
    width: 383px;
    height: 156px;
    background: linear-gradient(90deg, #3a3532 0%, #6f7c88 30%, #c9d6e0 55%, #b4c0ca 75%, #3d3834 100%);
  }
</style>
</head>
<body>
<div class="page">
  <div class="tile teal" style="left:447px;top:0;width:150px;height:150px"></div>
  <div class="tile green" style="left:597px;top:0;width:153px;height:150px"></div>
  <div class="tile mint" style="left:750px;top:0;width:150px;height:150px"></div>
  <div class="tile lime" style="left:750px;top:150px;width:150px;height:101px"></div>

  <div class="tile teal" style="left:750px;top:456px;width:150px;height:151px"></div>
  <div class="tile green" style="left:750px;top:607px;width:150px;height:150px"></div>
  <div class="tile mint" style="left:750px;top:757px;width:150px;height:154px"></div>
  <div class="tile teal-deep" style="left:750px;top:911px;width:150px;height:142px"></div>
  <div class="tile green" style="left:750px;top:1053px;width:150px;height:147px"></div>
  <div class="tile lime" style="left:600px;top:1053px;width:150px;height:147px"></div>

  <div class="tile lime" style="left:0;top:607px;width:149px;height:150px"></div>
  <div class="tile leaf" style="left:0;top:757px;width:149px;height:154px"></div>
  <div class="tile teal" style="left:0;top:911px;width:149px;height:142px"></div>
  <div class="tile olive" style="left:149px;top:911px;width:155px;height:142px"></div>
  <div class="tile mint" style="left:0;top:1053px;width:149px;height:147px"></div>
  <div class="tile leaf" style="left:149px;top:1053px;width:155px;height:147px"></div>
  <div class="tile moss" style="left:304px;top:1053px;width:149px;height:147px"></div>

  <h1 class="page-title">About the company</h1>

  <p class="intro">A basic brief about<br>your company.<br>Lumevara stages<br>events in the Kingdom</p>

  <div class="photo-frame">
    <div class="photo" role="img" aria-label="Photo of a speaker presenting on stage to a seated audience in front of a projection screen"></div>
  </div>

  <p class="body-copy">We conceptualize and stage<br>events and campaigns of all<br>sizes and calibres. As ex-<br>perts we keep strategic ties<br>and deep knowledge that let<br>us execute events at any le-<br>vel. Our service and commit-<br>ment set us apart, from con-<br>ception to completion.</p>
</div>
</body>
</html>
```